An international wholesale business needs letterhead design

Logo file is attached. Please design a letterhead with the following details:

- Company Name and Logo
- Address
- VAT Registration number
- Phone No
- Website address

```html
<!DOCTYPE html>
<html lang="en">
<head>
<meta charset="utf-8">
<title>Norvel Trading Letterhead</title>
<link href="https://fonts.googleapis.com/css2?family=Source+Sans+3:wght@400;600;700&display=swap" rel="stylesheet">
<style>
  :root {
    --backdrop: #e4e4e6;
    --paper: #ffffff;
    --brand-red: #c0202b;
    --deep-red: #9e1820;
    --band-grey: #8e9096;
    --text-grey: #6d6e72;
    --ink: #4a4b4f;
  }
  * { box-sizing: border-box; margin: 0; padding: 0; }
  html, body { width: 1200px; height: 800px; overflow: hidden; }
  body {
    background: var(--backdrop);
    font-family: "Source Sans 3", Arial, sans-serif;
    color: var(--text-grey);
  }
  .letterhead {
    position: absolute;
    left: 340px; top: 30px;
    width: 520px; height: 740px;
    background: var(--paper);
    box-shadow: 0 2px 10px rgba(0,0,0,0.12);
    overflow: hidden;
  }
  .brand {
    position: absolute; left: 44px; top: 42px;
    display: flex; align-items: center; gap: 8px;
    color: var(--brand-red);
    font-weight: 700; font-size: 24px; letter-spacing: 1px;
    text-transform: uppercase;
  }
  .brand-dot {
    width: 22px; height: 22px; border-radius: 50%;
    background: var(--brand-red);
  }
  .contact {
    position: absolute; right: 44px; top: 128px;
    list-style: none; font-size: 10.5px; line-height: 15px;
  }
  .contact li { display: flex; align-items: center; gap: 6px; }
  .contact svg { width: 11px; height: 11px; flex: none; }
  .date { position: absolute; left: 60px; top: 140px; font-size: 12px; }
  .recipient {
    position: absolute; left: 60px; top: 176px;
    font-size: 12px; line-height: 16px; font-style: normal;
  }
  .salutation {
    position: absolute; left: 60px; top: 268px;
    font-size: 12px; font-weight: 700; color: var(--ink);
  }
  .body-copy {
    position: absolute; left: 60px; top: 296px; width: 400px;
    font-size: 10.5px; line-height: 14px;
  }
  .body-copy p + p { margin-top: 12px; }
  .signature {
    position: absolute; right: 70px; top: 540px;
    width: 110px; height: 36px;
    background: linear-gradient(90deg, #f0f0f1, #dcdcde);
    border-radius: 4px;
  }
  .footer-band { position: absolute; left: 0; bottom: 0; width: 520px; height: 170px; }
  .footer-info {
    position: absolute; left: 38px; top: 632px;
    color: #fff; font-size: 9.5px; line-height: 12px;
  }
  .footer-info strong { font-size: 10.5px; letter-spacing: 0.5px; }
</style>
</head>
<body>
  <article class="letterhead">
    <header>
      <div class="brand"><span class="brand-dot"></span>Norvel Trading</div>
      <ul class="contact">
        <li><svg viewBox="0 0 12 12"><circle cx="6" cy="6" r="6" fill="var(--brand-red)"/><path d="M4 3.2l1 1.4-.6.7a4 4 0 0 0 2.3 2.3l.7-.6 1.4 1-.5 1c-2.6-.2-4.6-2.2-4.8-4.8z" fill="#fff"/></svg>(00) 01234 555 010</li>
        <li><svg viewBox="0 0 12 12"><circle cx="6" cy="6" r="6" fill="var(--brand-red)"/><rect x="3" y="4" width="6" height="4.2" fill="none" stroke="#fff" stroke-width="0.8"/><path d="M3 4l3 2.3L9 4" fill="none" stroke="#fff" stroke-width="0.8"/></svg>info@norveltrading.com</li>
        <li><svg viewBox="0 0 12 12"><circle cx="6" cy="6" r="6" fill="var(--brand-red)"/><circle cx="6" cy="6" r="3" fill="none" stroke="#fff" stroke-width="0.8"/><path d="M3 6h6M6 3c-1.5 1.8-1.5 4.2 0 6M6 3c1.5 1.8 1.5 4.2 0 6" fill="none" stroke="#fff" stroke-width="0.6"/></svg>www.norveltrading.com</li>
      </ul>
    </header>

    <p class="date">January 12, 2014</p>
    <address class="recipient">Mr. John Doe<br>President<br>BK Holdings<br>111 Street Name, Suite#<br>City, State, 12345</address>
    <p class="salutation">Dear Mr. John,</p>

    <div class="body-copy">
      <p>Lorem Ipsum is simply dummy text of the printing and typesetting industry. Lorem Ipsum has been the industry's standard dummy text ever since the 1500s, when an unknown printer took a galley of type and scrambled it to make a type specimen book. It has survived not only five centuries, but also the leap into electronic typesetting, remaining essentially unchanged.</p>
      <p>The standard chunk of Lorem Ipsum used since the 1500s is reproduced below for those interested. Sections 1.10.32 and 1.10.33 from "de Finibus Bonorum et Malorum" by Cicero are also reproduced in their exact original form, accompanied by English versions from the 1914 translation by H. Rackham.</p>
      <p>Lorem Ipsum is simply dummy text of the printing and typesetting industry. Lorem Ipsum has been the industry's standard dummy text ever since the 1500s, when an unknown printer took a galley of type and scrambled it to make a type specimen book. It has survived not only five centuries, but also the leap into electronic typesetting, remaining essentially unchanged. It was popularised in the</p>
    </div>

    <div class="signature" role="img" aria-label="Handwritten signature of the sender"></div>

    <footer>
      <svg class="footer-band" viewBox="0 0 520 170" preserveAspectRatio="none" aria-hidden="true">
        <path d="M0 30 C150 22 260 30 340 80 C410 124 470 150 520 156 L520 170 L0 170 Z" fill="var(--band-grey)"/>
        <path d="M0 38 C150 30 260 38 340 88 C410 132 470 156 520 160 L520 170 L0 170 Z" fill="#fff"/>
        <path d="M0 44 C150 36 260 44 340 94 C410 138 470 160 520 164 L520 170 L0 170 Z" fill="var(--brand-red)"/>
        <path d="M0 150 C160 144 320 150 520 170 L0 170 Z" fill="var(--deep-red)"/>
      </svg>
      <div class="footer-info">
        <strong>NORVEL TRADING</strong><br>
        Suite 102 Street name, State, Zip 2034, Country<br>
        VAT Reg. No.: 00000000000
      </div>
    </footer>
  </article>
</body>
</html>
```